New Business Card

Would like a shiny card with Metallic logo raised on th front. Address 418 Kestwick Lane, Toronto Ontario M4T2B8, phone 416 555 0382, email kmvc@lorentel.ca and web www.kmvc.ca on the back in right and left lower corners balanced. Top of back should say Personalized Care for Pet's and their People centered. Leaving space on the back to write. Horizontal placement

```html
<!DOCTYPE html>
<html lang="en">
<head>
<meta charset="utf-8">
<title>Kestwick Mill Veterinary Clinic – Business Card</title>
<link href="https://fonts.googleapis.com/css2?family=Work+Sans:wght@400;500&family=Michroma&display=swap" rel="stylesheet">
<style>
  :root {
    --stage: #1c1c1c;
    --card-light: #ffffff;
    --card-dark-a: #2a2a2a;
    --card-dark-b: #141414;
    --ink: #5a5a5a;
    --ink-soft: #6a6a6a;
    --paper-ink: #ffffff;
    --rule: #555555;
  }
  * { margin: 0; padding: 0; box-sizing: border-box; }
  html, body { width: 1200px; height: 897px; overflow: hidden; }
  body { background: var(--stage); position: relative; font-family: "Work Sans", sans-serif; }

  .card {
    position: absolute; left: 303px; width: 595px; height: 338px;
    border-radius: 24px; overflow: hidden;
  }
  .card--front { top: 92px; background: var(--card-light); color: var(--ink); }
  .card--back {
    top: 470px;
    background: radial-gradient(ellipse at 80% 30%, var(--card-dark-a), var(--card-dark-b) 75%);
    color: var(--paper-ink);
  }

  .brand { position: absolute; text-align: center; font-weight: 500; }
  .brand__mark { display: block; margin: 0 auto; border-radius: 50%; }
  .brand__name { display: block; letter-spacing: 1px; text-transform: uppercase; }

  .card--front .brand { left: 40px; width: 290px; top: 110px; color: var(--ink); }
  .card--front .brand__mark { width: 86px; height: 86px; background: var(--ink); margin-bottom: 12px; }
  .card--front .brand__name { font-size: 19px; line-height: 1.15; }
  .card--front .brand__name--sub { font-size: 11px; letter-spacing: 1.5px; }

  .divider { position: absolute; left: 343px; top: 97px; width: 2px; height: 147px; background: var(--rule); }

  .contact { position: absolute; left: 367px; top: 96px; }
  .contact__name { font-size: 18px; font-weight: 500; letter-spacing: 0.8px; color: var(--ink); }
  .contact__role { font-size: 15px; color: var(--ink-soft); margin-top: 2px; }
  .contact__address { font-size: 13.5px; line-height: 17px; margin-top: 14px; margin-left: 2px; color: var(--ink-soft); }
  .contact__list { list-style: none; margin-top: 12px; }
  .contact__item { display: flex; align-items: center; gap: 8px; font-size: 14px; line-height: 19px; color: var(--ink-soft); }
  .contact__icon { width: 11px; height: 11px; fill: var(--ink); flex: none; }

  .card--back .brand { left: 0; width: 595px; top: 86px; color: var(--paper-ink); }
  .card--back .brand__mark { width: 108px; height: 108px; background: var(--paper-ink); margin-bottom: 14px; }
  .card--back .brand__name { font-size: 25px; line-height: 1.1; }
  .card--back .brand__name--sub { font-size: 13px; letter-spacing: 2px; margin-top: 2px; }

  .tagline {
    position: absolute; left: 0; width: 595px; top: 278px; text-align: center;
    font-family: "Michroma", sans-serif; font-size: 13px; line-height: 20px;
    letter-spacing: 1.5px; text-transform: uppercase;
  }
</style>
</head>
<body>
  <section class="card card--front">
    <div class="brand">
      <span class="brand__mark"></span>
      <span class="brand__name">Kestwick Mill</span>
      <span class="brand__name brand__name--sub">Veterinary Clinic</span>
    </div>
    <div class="divider"></div>
    <div class="contact">
      <p class="contact__name">DORIAN VALE</p>
      <p class="contact__role">Founder</p>
      <p class="contact__address">418 Kestwick Lane,<br>Toronto Ontario M4T2B8</p>
      <ul class="contact__list">
        <li class="contact__item">
          <svg class="contact__icon" viewBox="0 0 24 24"><path d="M6.6 10.8a15 15 0 0 0 6.6 6.6l2.2-2.2c.3-.3.7-.4 1-.2 1.1.4 2.3.6 3.6.6.6 0 1 .4 1 1V20c0 .6-.4 1-1 1C10.6 21 3 13.4 3 4c0-.6.4-1 1-1h3.5c.6 0 1 .4 1 1 0 1.3.2 2.5.6 3.6.1.3 0 .7-.2 1z"/></svg>
          416 555 0382
        </li>
        <li class="contact__item">
          <svg class="contact__icon" viewBox="0 0 24 24"><path d="M2 5h20v2l-10 6L2 7zM2 9l10 6 10-6v10H2z"/></svg>
          kmvc@lorentel.ca
        </li>
        <li class="contact__item">
          <svg class="contact__icon" viewBox="0 0 24 24" fill="none" stroke="currentColor" stroke-width="2"><circle cx="12" cy="12" r="10"/><path d="M2 12h20M12 2c3 3 3 17 0 20M12 2c-3 3-3 17 0 20"/></svg>
          www.kmvc.ca
        </li>
      </ul>
    </div>
  </section>

  <section class="card card--back">
    <div class="brand">
      <span class="brand__mark"></span>
      <span class="brand__name">Kestwick Mill</span>
      <span class="brand__name brand__name--sub">Veterinary Clinic</span>
    </div>
    <p class="tagline">Personalized care for pet's<br>and their people centered</p>
  </section>
</body>
</html>
```